Orlindo Community In Marrowdale Website Design

The Orlindo Community In Marrowdale is a community organization that promotes the welfare of people of Kenyan descent living in Marrowdale. We would like a website designed and coded for the community.
Please refer to the attached document for the brief.

Target Market(s)

Kenyan-Americans living in the State of Marrowdale

Industry/Entity Type

Non-Profit Community Welfare group

Coding

Coded - Design and coding required

Number of Pages Required

1 page

Font styles to use
Other font styles liked:
• Open Sans

Requirements
Must have
• A private members page; calendar feature or a message board; ability to accept payments
Nice to have
• Ability to maintain a members register

```html
<!DOCTYPE html>
<html lang="en">
<head>
<meta charset="utf-8">
<title>Orlindo Community In Marrowdale</title>
<link rel="stylesheet" href="https://fonts.googleapis.com/css2?family=Montserrat:wght@500;600;700;800&family=Open+Sans:wght@400;600;700&display=swap">
<style>
:root{
  --red:#bf0000;
  --red-soft:#f6dede;
  --green:#0b640b;
  --green-soft:#cfe0cd;
  --ink:#111111;
  --text:#2b2b2b;
  --grey:#e9e9e9;
  --white:#ffffff;
}
*{box-sizing:border-box;margin:0;padding:0}
html,body{width:1200px;height:4051px;overflow:hidden}
body{position:relative;background:var(--white);font-family:"Open Sans",Arial,sans-serif;color:var(--text)}
.abs{position:absolute}
.head{font-family:"Montserrat",Arial,sans-serif;color:var(--ink);font-weight:700}
.btn-dark{position:absolute;background:var(--ink);color:#fff;border-radius:7px;font-size:12px;display:flex;align-items:center;justify-content:center;font-family:"Open Sans",Arial,sans-serif;text-transform:uppercase}
.photo{position:absolute;overflow:hidden}

/* header */
.site-header{position:absolute;left:0;top:0;width:1200px;height:75px;background:#fff}
.brand{position:absolute;left:78px;top:8px;width:190px;height:60px;display:flex;align-items:center;gap:8px}
.brand-mark{width:56px;height:56px;border:2px solid var(--ink);border-radius:50%;flex:none}
.brand-name{font-family:"Montserrat",Arial,sans-serif;font-weight:600;font-size:11px;line-height:1.25;color:var(--ink);width:120px}
.nav{position:absolute;left:225px;top:28px;display:flex;gap:19px;font-size:13px;color:var(--ink)}
.nav span.drop::after{content:"";display:inline-block;margin-left:6px;border:4px solid transparent;border-top:5px solid var(--ink);vertical-align:1px}
.nav-btn{position:absolute;top:19px;height:39px;border:1.5px solid var(--red);border-radius:8px;color:var(--red);font-size:14px;display:flex;align-items:center;justify-content:center;letter-spacing:.3px}

/* hero */
.hero{position:absolute;left:0;top:75px;width:1200px;height:497px;overflow:hidden;background:linear-gradient(180deg,#9fa1a3 0%,#8e8f8c 45%,#5d5a52 75%,#3e3a32 100%)}
.hero-title{position:absolute;left:77px;top:275px;font-family:"Montserrat",Arial,sans-serif;font-weight:800;font-size:96px;color:#fff;line-height:1}
.hero-sub{position:absolute;left:77px;top:376px;font-family:"Montserrat",Arial,sans-serif;font-weight:600;font-size:35px;color:#fff}
.dots{position:absolute;left:82px;top:434px;display:flex;gap:10px}
.dots i{display:block;width:20px;height:4px;border:1px solid #fff;border-radius:2px}
.dots i.on{background:var(--red);border-color:var(--red)}

/* story */
.eyebrow{font-family:"Montserrat",Arial,sans-serif;font-weight:700;font-size:13px;color:var(--ink)}
.story-text{position:absolute;left:698px;top:778px;width:390px;font-size:15px;line-height:22.5px}

/* initiatives */
.initiatives{position:absolute;left:0;top:1109px;width:1200px;height:637px}
.init-title{position:absolute;left:0;top:90px;width:1200px;text-align:center;font-family:"Montserrat",Arial,sans-serif;font-weight:700;font-size:48px;color:#fff}
.init-lead{position:absolute;left:250px;top:146px;width:700px;text-align:center;color:#fff;font-size:15px;line-height:22.5px}
.card{position:absolute;top:250px;width:252px;height:293px;background:#fff;border-radius:18px;text-align:center}
.card svg{position:absolute;left:99px;top:28px}
.card h3{position:absolute;left:0;top:102px;width:100%;font-family:"Montserrat",Arial,sans-serif;font-weight:700;font-size:15px;line-height:19px;color:var(--ink)}
.card p{position:absolute;left:24px;top:145px;width:204px;font-size:12.5px;line-height:19.5px;color:#333}
.card .more{position:absolute;left:75px;top:238px;width:102px;height:32px;background:var(--green);color:#fff;border-radius:7px;font-size:11.5px;display:flex;align-items:center;justify-content:center}

/* membership */
.member-title{position:absolute;left:0;top:1820px;width:1200px;text-align:center;font-family:"Montserrat",Arial,sans-serif;font-weight:700;font-size:50px;line-height:57px;color:var(--ink)}
.accent{color:var(--red)}
.member-lead{position:absolute;left:330px;top:1943px;width:540px;text-align:center;font-size:15px;line-height:22.5px}
.perk{position:absolute;left:77px;width:500px}
.perk svg{position:absolute;left:0;top:0}
.perk h4{position:absolute;left:77px;top:0;font-family:"Montserrat",Arial,sans-serif;font-weight:700;font-size:17px}
.perk p{position:absolute;left:77px;top:29px;width:420px;font-size:15.5px;line-height:24px}

/* welfare */
.welfare-title{position:absolute;left:678px;top:2632px;font-family:"Montserrat",Arial,sans-serif;font-weight:700;font-size:47px;line-height:57px;color:var(--ink)}
.welfare-text{position:absolute;left:678px;top:2812px;width:450px;font-size:14.5px;line-height:22.5px}

/* newsletter */
.connect{position:absolute;left:0;top:3099px;width:1200px;height:506px}
.connect-title{position:absolute;left:0;top:90px;width:1200px;text-align:center;font-family:"Montserrat",Arial,sans-serif;font-weight:700;font-size:48px;color:#fff}
.connect-lead{position:absolute;left:350px;top:156px;width:500px;text-align:center;color:#fff;font-size:15px;line-height:22.5px}
.signup{position:absolute;left:225px;top:262px;width:750px;height:52px;background:#fff;border-radius:7px}
.signup .field{position:absolute;left:38px;top:16px;font-size:14px;color:#777}
.signup .go{position:absolute;right:5px;top:5px;width:112px;height:42px;background:var(--ink);color:#fff;border-radius:7px;font-size:12px;display:flex;align-items:center;justify-content:center}
.terms{position:absolute;left:0;top:352px;width:1200px;text-align:center;color:#fff;font-size:14px;line-height:24px}
.terms b{font-weight:600}

/* footer */
.site-footer{position:absolute;left:0;top:3605px;width:1200px;height:446px;background:var(--grey)}
.foot-h{position:absolute;top:98px;font-family:"Montserrat",Arial,sans-serif;font-weight:700;font-size:19px;color:var(--ink)}
.links{position:absolute;left:436px;top:129px;font-size:15px;line-height:28.6px;color:var(--ink);list-style:none}
.contact-item{position:absolute;left:610px;font-size:15px;color:var(--ink);line-height:22px}
.contact-item b{display:block;font-weight:700;font-size:14px;margin-left:20px}
.contact-item span{display:block;margin-left:20px}
.contact-item svg{position:absolute;left:0;top:3px}
.social{position:absolute;top:124px;width:38px;height:38px;border:1.5px solid var(--ink);border-radius:50%}
.rule{position:absolute;left:66px;top:384px;width:1067px;height:1px;background:#c9c9c9}
.copy{position:absolute;left:0;top:405px;width:1200px;text-align:center;font-size:13.5px;color:var(--ink)}
</style>
</head>
<body>

<header class="site-header">
  <div class="brand"><span class="brand-mark"></span><span class="brand-name">Orlindo Community In Marrowdale</span></div>
  <nav class="nav">
    <span>Home</span><span class="drop">About us</span><span class="drop">Our Initiatives</span><span class="drop">Events</span><span class="drop">Media</span><span class="drop">Get Involve</span><span class="drop">Member Portal</span>
  </nav>
  <div class="nav-btn" style="left:887px;width:102px">LOGIN</div>
  <div class="nav-btn" style="left:1000px;width:117px">DONATE</div>
</header>

<section class="hero" role="img" aria-label="City skyline with a domed capitol building at dusk">
  <svg class="abs" style="left:0;top:0" width="1200" height="497" viewBox="0 0 1200 497">
    <path d="M1200,185 C1160,380 1030,470 880,497 L1200,497 Z" fill="#d9d9d9"/>
    <path d="M1200,300 C1160,420 1060,480 960,497 L1200,497 Z" fill="#ffffff"/>
  </svg>
  <div class="hero-title">ORLINDO</div>
  <div class="hero-sub">Community In Marrowdale</div>
  <div class="dots"><i></i><i class="on"></i><i></i></div>
</section>

<section class="story">
  <svg class="abs" style="left:100px;top:630px" width="550" height="410" viewBox="0 0 550 410">
    <line x1="10" y1="205" x2="537" y2="205" stroke="#111" stroke-width="2"/>
    <circle cx="274" cy="205" r="194" fill="#fff" stroke="#111" stroke-width="3"/>
    <circle cx="274" cy="205" r="134" fill="#8fb4d6"/>
  </svg>
  <div class="photo" role="img" aria-label="Smiling woman holding a flag outstretched against a blue sky" style="left:240px;top:701px;width:268px;height:268px;border-radius:50%;background:linear-gradient(180deg,#a9c8e3 0%,#d8dfe6 45%,#c41f2a 62%,#111 72%,#1d7a34 85%,#e4e4e4 100%)"></div>
  <div class="abs" style="left:174px;top:1000px;width:400px;text-align:center;font-family:'Montserrat',Arial,sans-serif;font-weight:600;font-size:13px;color:#111;letter-spacing:2px">ORLINDO COMMUNITY IN MARROWDALE</div>

  <div class="eyebrow abs" style="left:698px;top:693px">OUR JOURNEY</div>
  <h2 class="head abs" style="left:698px;top:710px;font-size:48px"><span class="accent">OUR</span> STORY</h2>
  <p class="story-text">As a non-profit organization dedicated to uniting Orlindans in Marrowdale, we cherish the strong relationships we've built with our community over the years. We are committed to providing exceptional service to all our members. Explore our site to discover more about what we offer.</p>
  <div class="btn-dark" style="left:698px;top:933px;width:147px;height:41px">Discover More</div>
</section>

<section class="initiatives">
  <svg class="abs" style="left:0;top:0" width="1200" height="637" viewBox="0 0 1200 637">
    <path d="M0,637 L0,170 C50,55 160,0 290,0 L330,0 L0,637 Z" fill="var(--red-soft)"/>
    <path d="M0,637 L0,265 C45,95 160,0 307,0 L1200,0 L1200,637 Z" fill="var(--red)"/>
  </svg>
  <h2 class="init-title">OUR INITIATIVES</h2>
  <p class="init-lead">OCIM has built a positive reputation by delivering exceptional service to our community. We understand the importance of adapting quickly to meet your changing needs. Learn more about how we can assist you.</p>

  <article class="card" style="left:77px">
    <svg width="54" height="58" viewBox="0 0 54 58" fill="none" stroke="#c00000" stroke-width="2"><rect x="4" y="2" width="46" height="30" rx="3"/><line x1="4" y1="10" x2="50" y2="10"/><path d="M27 14l3 6 6 1-4 4 1 6-6-3-6 3 1-6-4-4 6-1z"/><circle cx="14" cy="40" r="5"/><circle cx="40" cy="40" r="5"/><circle cx="27" cy="38" r="5"/><path d="M5 56c0-8 4-10 9-10s9 2 9 10M31 56c0-8 4-10 9-10s9 2 9 10M18 56c0-9 4-11 9-11s9 2 9 11"/></svg>
    <h3>CULTURAL<br>EVENTS</h3>
    <p>OCIM organizes annual events that celebrate Orlindo and its rich diversity. Some of the cultural events we organize...</p>
    <div class="more">READ MORE</div>
  </article>
  <article class="card" style="left:344px">
    <svg width="56" height="58" viewBox="0 0 56 58" fill="none" stroke="#c00000" stroke-width="2"><rect x="3" y="2" width="34" height="26" rx="2"/><line x1="10" y1="22" x2="10" y2="14"/><line x1="16" y1="22" x2="16" y2="10"/><line x1="22" y1="22" x2="22" y2="16"/><circle cx="44" cy="14" r="6"/><path d="M34 34c0-8 4-11 10-11s10 3 10 11"/><rect x="3" y="34" width="50" height="6"/><circle cx="14" cy="46" r="4"/><circle cx="28" cy="46" r="4"/><circle cx="42" cy="46" r="4"/><path d="M6 57c0-4 4-6 8-6s8 2 8 6M20 57c0-4 4-6 8-6s8 2 8 6M34 57c0-4 4-6 8-6s8 2 8 6"/></svg>
    <h3>EDUCATIONAL<br>WORKSHOP</h3>
    <p>Recognizing the need to provide educational opportunities for the Orlindo Community we hold Youth workshops...</p>
    <div class="more">READ MORE</div>
  </article>
  <article class="card" style="left:612px">
    <svg width="56" height="58" viewBox="0 0 56 58" fill="none" stroke="#c00000" stroke-width="2"><circle cx="10" cy="12" r="7"/><circle cx="28" cy="8" r="7"/><circle cx="46" cy="12" r="7"/><path d="M28 4v8M25 6h6M25 10h6"/><path d="M4 30c4 4 8 12 10 20h8l2-10c-3-6-8-8-12-10M52 30c-4 4-8 12-10 20h-8l-2-10c3-6 8-8 12-10"/><path d="M28 26l-4 4 4 4 4-4z"/></svg>
    <h3>SUPPORT<br>INITIATIVES</h3>
    <p>We realize that unplanned life events such as death may happen. For that reason we created a welfare...</p>
    <div class="more">READ MORE</div>
  </article>
  <article class="card" style="left:879px">
    <svg width="56" height="58" viewBox="0 0 56 58" fill="none" stroke="#c00000" stroke-width="2"><circle cx="28" cy="10" r="6"/><circle cx="12" cy="40" r="6"/><circle cx="44" cy="40" r="6"/><path d="M18 22c0-3 4-5 10-5s10 2 10 5M2 54c0-5 4-7 10-7s10 2 10 7M34 54c0-5 4-7 10-7s10 2 10 7" /><path d="M22 20l-8 14M34 20l8 14M20 44h16" stroke-dasharray="3 3"/></svg>
    <h3>STAYING<br>CONNECTED</h3>
    <p>Staying connected is essential for the Orlindo Community in Marrowdale we cherish the strong relationships...</p>
    <div class="more">READ MORE</div>
  </article>
</section>

<section class="membership">
  <h2 class="member-title">GET INVOLVED WITH<br>OC <span class="accent">MEMBERSHIP</span></h2>
  <p class="member-lead">There are many ways to get involved with and contribute to our vibrant community:</p>

  <div class="perk" style="top:2072px">
    <svg width="64" height="56" viewBox="0 0 64 56" fill="none"><circle cx="44" cy="40" r="14" fill="#f4d6d6"/><g stroke="#c00000" stroke-width="2"><circle cx="24" cy="12" r="7"/><circle cx="11" cy="17" r="5"/><circle cx="37" cy="17" r="5"/><path d="M12 40c0-10 5-16 12-16s12 6 12 16zM2 38c0-8 3-12 9-12M46 38c0-8-3-12-9-12"/></g></svg>
    <h4 class="accent">BECOME A MEMBER:</h4>
    <p>Join our community to access. exclusive events, member benefits, and a supportive network of friends.</p>
  </div>
  <div class="perk" style="top:2193px">
    <svg width="64" height="56" viewBox="0 0 64 56" fill="none"><circle cx="44" cy="38" r="14" fill="#d7e6d5"/><g stroke="#0b640b" stroke-width="2"><rect x="4" y="4" width="38" height="34" rx="2"/><line x1="4" y1="11" x2="42" y2="11"/><path d="M12 1v6M34 1v6"/><circle cx="23" cy="20" r="4"/><path d="M14 34c0-6 4-8 9-8s9 2 9 8"/></g></svg>
    <h4 style="color:var(--green)">ATTEND EVENT:</h4>
    <p>From family-friendly picnics to educational workshops &amp; community outreach programs. there's always something happening at.</p>
  </div>
  <div class="perk" style="top:2338px">
    <svg width="64" height="56" viewBox="0 0 64 56" fill="none"><circle cx="44" cy="38" r="14" fill="#dedede"/><g stroke="#111" stroke-width="2"><path d="M23 40C8 30 4 22 4 14a9 9 0 0 1 19-4 9 9 0 0 1 19 4c0 8-4 16-19 26z"/><circle cx="17" cy="18" r="3"/><circle cx="29" cy="18" r="3"/><path d="M11 30c0-4 3-6 6-6s6 2 6 6M23 30c0-4 3-6 6-6s6 2 6 6"/></g></svg>
    <h4>VOLUNTEER:</h4>
    <p>Give back to the community by volunteering your time and skills to help organise events, mentor newcomers, or support community initiatives.</p>
  </div>
  <div class="btn-dark" style="left:77px;top:2457px;width:212px;height:40px">Register for Membership</div>

  <div class="photo" role="img" aria-label="Elephant walking on a dirt road with a safari vehicle behind" style="left:629px;top:2122px;width:368px;height:368px;border-radius:50%;background:linear-gradient(180deg,#eef1ec 0%,#9aa87a 35%,#6b6a5a 60%,#a7927a 100%);box-shadow:0 14px 30px rgba(0,0,0,.15)"></div>
  <div class="photo" role="img" aria-label="Colourful bird in flight over dry grass" style="left:844px;top:2054px;width:274px;height:174px;border-radius:50%;border:4px solid #fff;background:radial-gradient(circle at 45% 45%,#4fa8d8 0%,#6bb6b9 25%,#c9a55a 60%,#8c6f3a 100%)"></div>
</section>

<section class="welfare">
  <svg class="abs" style="left:0;top:2897px" width="62" height="120" viewBox="0 0 62 120"><path d="M0,0 A60,60 0 0 1 0,120 Z" fill="var(--red)"/></svg>
  <div class="photo" role="img" aria-label="Elephant family walking through golden grassland" style="left:96px;top:2567px;width:402px;height:402px;border-radius:50%;background:linear-gradient(180deg,#e9e2d4 0%,#b8a58a 45%,#7b6a55 60%,#c9a060 80%,#b88a45 100%)"></div>
  <div class="photo" role="img" aria-label="Hand holding a smartphone" style="left:386px;top:2843px;width:184px;height:184px;border-radius:50%;border:4px solid #fff;background:linear-gradient(135deg,#e7e2dc 0%,#c9bdb1 50%,#9b8a7a 100%)"></div>

  <h2 class="welfare-title">BE PART OF OC<br><span class="accent">WELFARE</span> OC<br>FAMILY WELFARE</h2>
  <p class="welfare-text">With OC Welfare, financial assistance is provided to members in the unfortunate event of a death within their nuclear family (including father, mother/guardian, brother, sister, spouse, son, or daughter) or in the case of the member's own death.</p>
  <div class="btn-dark" style="left:678px;top:2911px;width:130px;height:40px">Join Welfare</div>
</section>

<section class="connect">
  <svg class="abs" style="left:0;top:0" width="1200" height="506" viewBox="0 0 1200 506">
    <path d="M0,0 L960,0 C1110,20 1200,110 1200,170 L1200,506 L0,506 Z" fill="var(--green-soft)"/>
    <path d="M0,0 L880,0 C1070,0 1185,110 1200,280 L1200,506 L0,506 Z" fill="var(--green)"/>
  </svg>
  <h2 class="connect-title">STAY CONNECTED</h2>
  <p class="connect-lead">Subscribe to our newsletter and be the first to know about our latest updates, exclusive offers, and insightful content delivered right to your inbox.</p>
  <div class="signup">
    <svg class="abs" style="left:18px;top:20px" width="15" height="12" viewBox="0 0 15 12"><rect width="15" height="12" rx="1.5" fill="#999"/><path d="M1 1.5l6.5 5 6.5-5" stroke="#fff" stroke-width="1.3" fill="none"/></svg>
    <span class="field">Enter your email address</span>
    <div class="go">SUBSCRIBE</div>
  </div>
  <p class="terms">By subscribing, you agree with MailPost's <b>Terms of Service</b> and<br><b>Privacy Policy</b></p>
</section>

<footer class="site-footer">
  <svg class="abs" style="left:76px;top:110px" width="284" height="210" viewBox="0 0 284 210"><line x1="0" y1="105" x2="284" y2="105" stroke="#111" stroke-width="1.5"/><circle cx="141" cy="105" r="102" fill="var(--grey)" stroke="#111" stroke-width="2.5"/></svg>
  <div class="abs" style="left:137px;top:195px;width:160px;text-align:center;font-family:'Montserrat',Arial,sans-serif;font-weight:600;font-size:14px;line-height:19px;color:#111">Orlindo Community In Marrowdale</div>

  <h3 class="foot-h" style="left:433px">QUICK LINKS</h3>
  <ul class="links"><li>Home</li><li>Welcome</li><li>About</li><li>Services</li><li>Shop</li><li>Groups</li><li>Contact Us</li></ul>

  <h3 class="foot-h" style="left:610px">CONTACT US</h3>
  <div class="contact-item" style="top:128px">
    <svg width="13" height="13" viewBox="0 0 24 24"><path fill="#c00000" d="M6.6 10.8a15.1 15.1 0 0 0 6.6 6.6l2.2-2.2c.3-.3.7-.4 1-.2 1.1.4 2.3.6 3.6.6.6 0 1 .4 1 1V20c0 .6-.4 1-1 1A17 17 0 0 1 3 4c0-.6.4-1 1-1h3.5c.6 0 1 .4 1 1 0 1.3.2 2.5.6 3.6.1.3 0 .7-.2 1z"/></svg>
    <b>PHONE</b><span>+1 555-014-2290</span>
  </div>
  <div class="contact-item" style="top:190px">
    <svg width="13" height="11" viewBox="0 0 15 12"><rect width="15" height="12" rx="1.5" fill="#c00000"/><path d="M1 1.5l6.5 5 6.5-5" stroke="#fff" stroke-width="1.3" fill="none"/></svg>
    <b>EMAIL</b><span>ocim2024@example.org</span>
  </div>
  <div class="contact-item" style="top:252px">
    <svg width="12" height="15" viewBox="0 0 24 30"><path fill="#c00000" d="M12 0a11 11 0 0 0-11 11c0 8 11 19 11 19s11-11 11-19A11 11 0 0 0 12 0zm0 15a4 4 0 1 1 0-8 4 4 0 0 1 0 8z"/></svg>
    <b>ADDRESS</b><span>48 Fernhollow Drive Marrowdale, ZZ<br>00000</span>
  </div>

  <h3 class="foot-h" style="left:878px">SOCIAL MEDIA</h3>
  <span class="social" style="left:878px" aria-label="Social profile one"></span>
  <span class="social" style="left:927px" aria-label="Social profile two"></span>
  <span class="social" style="left:976px" aria-label="Social profile three"></span>
  <span class="social" style="left:1025px" aria-label="Social profile four"></span>

  <div class="rule"></div>
  <p class="copy">© Copyright Orlindo Community In Marrowdale</p>
</footer>

</body>
</html>
```